Touch screen based web site design

We have a product called vTrellis.

It is a browser based touch screen application for the apartment leasing industry . You can read more about it at http://vtrellis.korvathsoft.example.

To see how the product functions, you can check the link http://www.webvtrellis.example/vtrellis.aspx?k=demo1.

We have a need to give a new look and feel to the application. The redesign is NOT to be limited to colors and shapes, but an overhaul of the screen layout, color, font scheme to make the application flow nice and smooth. The content of the pages will remain the same.

There will be animations but that can be done by our IT team, if described in concept by the designer.

Again to reiterate, all things are up for grab, do not get influenced by the images, shapes and color used currently.

Reason: None of the design are coming even close to what I am asking for. Please see the homepage of the application at http://www.korvathsoft.example/vtrellis/images/img-screenshot-lg-01.jpg. That is what I am asking for as the first page to show the design idea.

Reason: At least the last couple of designs submitted understands it is a touch screen and the home page is not a web site home page. The reason I am still not able to select a design is that the quality of graphic design elements is sub par. For example, The treatment to the options for example are not sharp and up to mark.

Target Market(s)

Propective residents walking into a apartment leasing centers

Industry/Entity Type

Apartment

Requirements
Must have
• - Must have a design where the content, like name of the property, menu options and pictures, are dynamic. So for example, do not restrict the design in a manner that we cannot switch off an option without redesign of the page.
- Good use of icons for options
- Gives the user a calm and serene feeling while maintaining a crisp modern user interface
Nice to have
• - Design in a manner that the background can be a custom image for a specific client
- Description of animation on the screen where the images selected by the client can rotate/slide/appear/animate
Should not have
• - Boxy design
- Small options that cannot be touched by fingers
- dont plan on hover animations, will not work in touch

```html
<!DOCTYPE html>
<html lang="en">
<head>
<meta charset="utf-8">
<title>vTrellis — Touch Home</title>
<link rel="stylesheet" href="https://fonts.googleapis.com/css2?family=Great+Vibes&family=Cormorant+Garamond:wght@500&family=Roboto+Condensed:wght@300;400&family=Quicksand:wght@500&display=swap">
<style>
  :root {
    --bg-top: #f7f7f7;
    --bg-bottom: #e4e4e4;
    --ink: #333333;
    --ink-soft: #6b6b6b;
    --script: #5a5a5a;
    --headline: #5e5252;
    --tab-dark: #2f2f2f;
    --tab-mid: #5a5a5a;
    --green-light: #b6de3f;
    --green: #8cc420;
    --green-dark: #6fa312;
    --icon-ink: #eef8d8;
    --frame: #fbf8f3;
  }
  * { box-sizing: border-box; margin: 0; padding: 0; }
  html, body { width: 1200px; height: 662px; overflow: hidden; }
  body {
    position: relative;
    background: linear-gradient(180deg, var(--bg-top) 0%, #f1f1f1 55%, var(--bg-bottom) 100%);
    font-family: "Roboto Condensed", "Arial Narrow", sans-serif;
    color: var(--ink);
  }

  .brand-tab {
    position: absolute; left: 0; top: 0;
    width: 152px; height: 54px;
    background: linear-gradient(180deg, var(--tab-mid), var(--tab-dark));
    border-radius: 0 0 8px 0;
    box-shadow: 0 2px 4px rgba(0,0,0,.35);
    display: flex; align-items: center; justify-content: center;
  }
  .brand-tab__name {
    font-family: "Quicksand", sans-serif; font-weight: 500;
    font-size: 28px; color: #ffffff; letter-spacing: .5px;
  }
  .brand-caption {
    position: absolute; left: 5px; top: 57px;
    font-family: Arial, Helvetica, sans-serif; font-size: 9px; color: #333;
  }

  .tagline {
    position: absolute; left: 0; right: 0; top: 10px;
    text-align: center;
    font-family: "Great Vibes", cursive;
    font-size: 33px; color: var(--script);
    text-shadow: 0 2px 3px rgba(0,0,0,.18);
  }

  .slide {
    position: absolute; top: 111px; height: 332px;
    border: 3px solid var(--frame);
    border-radius: 6px;
    box-shadow: 0 3px 6px rgba(0,0,0,.22);
  }
  .slide--prev {
    left: -6px; width: 158px;
    background: linear-gradient(160deg, #f08a1c 0%, #8cc43a 35%, #5fa528 55%, #e9572c 80%, #f39a2a 100%);
  }
  .slide--next {
    left: 1044px; width: 170px;
    background: linear-gradient(180deg, #8fb4d6 0%, #dfe4e6 22%, #c2a58a 32%, #33a4e6 45%, #1d8fdc 75%, #c9b8a5 100%);
  }
  .slide--current {
    left: 258px; width: 684px;
    background: linear-gradient(180deg, #e6e1df 0%, #ece7e4 60%, #c99a72 70%, #d9ae86 100%);
  }
  .slide__photo { position: absolute; inset: 0; }
  .slide__caption {
    position: absolute; right: 18px; top: 34px; width: 230px;
    text-align: center; color: var(--headline);
    font-family: "Cormorant Garamond", Georgia, serif; font-weight: 500;
  }
  .slide__title { font-size: 40px; line-height: 1.1; text-align: right; }
  .slide__text { font-size: 18px; line-height: 1.05; margin-top: 10px; }

  .reflection {
    position: absolute; top: 447px; height: 80px; opacity: .22;
    border-radius: 6px;
    -webkit-mask-image: linear-gradient(180deg, #000, transparent);
            mask-image: linear-gradient(180deg, #000, transparent);
  }
  .reflection--prev { left: -6px; width: 158px; background: linear-gradient(180deg, #f39a2a, #e9572c); }
  .reflection--current { left: 258px; width: 684px; background: linear-gradient(180deg, #d9ae86, #e6e1df); }
  .reflection--next { left: 1044px; width: 170px; background: linear-gradient(180deg, #c9b8a5, #8fb4d6); }

  .prompt {
    position: absolute; left: 0; right: 0; top: 459px;
    text-align: center; font-weight: 300; font-size: 40px; color: var(--ink);
  }

  .menu {
    position: absolute; left: 0; right: 0; top: 526px;
    display: flex; justify-content: center; gap: 70px;
    list-style: none;
  }
  .menu__item { width: 86px; display: flex; flex-direction: column; align-items: center; }
  .menu__tile {
    width: 86px; height: 86px; border-radius: 4px;
    background: linear-gradient(180deg, var(--green-light) 0%, var(--green) 55%, var(--green-dark) 100%);
    box-shadow: 0 2px 3px rgba(0,0,0,.3), inset 0 1px 0 rgba(255,255,255,.45);
    display: flex; align-items: center; justify-content: center;
  }
  .menu__tile svg { width: 64px; height: 64px; }
  .menu__logo-text {
    font-family: "Quicksand", sans-serif; font-weight: 500;
    font-size: 21px; line-height: 1.25; color: var(--icon-ink); text-align: center;
  }
  .menu__label {
    margin-top: 10px; font-size: 20px; font-weight: 400; color: var(--ink-soft);
    white-space: nowrap;
  }
</style>
</head>
<body>
  <header>
    <div class="brand-tab"><span class="brand-tab__name">vTrellis</span></div>
    <p class="brand-caption">Logo of company using vTrellis here</p>
    <p class="tagline">When you’re here you know you have arrived .</p>
  </header>

  <section class="carousel">
    <div class="slide slide--prev"><div class="slide__photo" role="img" aria-label="Photo of fresh citrus fruit, kiwi and green apples"></div></div>
    <div class="slide slide--current">
      <div class="slide__photo" role="img" aria-label="Photo of two residents meditating in a fitness studio"></div>
      <div class="slide__caption">
        <p class="slide__title">Words here.</p>
        <p class="slide__text">Some text of company using vTrellis</p>
      </div>
    </div>
    <div class="slide slide--next"><div class="slide__photo" role="img" aria-label="Photo of a resort swimming pool with lounge chairs"></div></div>
    <div class="reflection reflection--prev"></div>
    <div class="reflection reflection--current"></div>
    <div class="reflection reflection--next"></div>
  </section>

  <p class="prompt">Touch an option below to explore!</p>

  <ul class="menu">
    <li class="menu__item">
      <div class="menu__tile">
        <svg viewBox="0 0 64 64" fill="var(--icon-ink)">
          <circle cx="32" cy="10" r="5"/><circle cx="14" cy="20" r="5"/><circle cx="50" cy="20" r="5"/>
          <path d="M27 17h10l-1 20h-3l-1 14h0l-1-14h-3z"/>
          <path d="M9 27h10l-1 14h-2l-1 13h-2l-1-13h-2z"/>
          <path d="M45 27h10l-1 14h-2l-1 13h-2l-1-13h-2z"/>
          <path d="M18 28l9-8 2 2-9 9zM46 28l-9-8-2 2 9 9z"/>
          <path d="M22 52h20v3H22z"/>
        </svg>
      </div>
      <span class="menu__label">Community</span>
    </li>
    <li class="menu__item">
      <div class="menu__tile">
        <svg viewBox="0 0 64 64" fill="var(--icon-ink)">
          <path d="M4 30 18 16l14 14v4H4z"/>
          <path d="M30 26 44 12l16 14v4H30z"/>
          <rect x="7" y="33" width="22" height="16"/>
          <rect x="33" y="29" width="24" height="20"/>
          <path d="M4 56c14-6 26 2 40-6 6-3 12-3 16-2v6H4z" fill="var(--green)" stroke="var(--icon-ink)" stroke-width="3"/>
          <rect x="38" y="34" width="5" height="5" fill="var(--green)"/><rect x="47" y="34" width="5" height="5" fill="var(--green)"/>
          <rect x="12" y="37" width="5" height="5" fill="var(--green)"/>
        </svg>
      </div>
      <span class="menu__label">Neighborhood</span>
    </li>
    <li class="menu__item">
      <div class="menu__tile">
        <svg viewBox="0 0 64 64" fill="none" stroke="var(--icon-ink)" stroke-width="4">
          <rect x="8" y="8" width="48" height="48"/>
          <path d="M26 8v14M26 30v8h-18M26 46v10M36 8v18h20M36 34v10h8M44 34v-8M36 44v12"/>
        </svg>
      </div>
      <span class="menu__label">Floor Plans</span>
    </li>
    <li class="menu__item">
      <div class="menu__tile">
        <svg viewBox="0 0 64 64" fill="none" stroke="var(--icon-ink)" stroke-width="4" stroke-linejoin="round">
          <rect x="6" y="15" width="52" height="34" fill="var(--icon-ink)"/>
          <path d="M6 15l26 20 26-20M6 49l19-17M58 49 39 32" stroke="var(--green)" stroke-width="3"/>
        </svg>
      </div>
      <span class="menu__label">Contact</span>
    </li>
    <li class="menu__item">
      <div class="menu__tile"><span class="menu__logo-text">Logo<br>Here</span></div>
      <span class="menu__label">Company</span>
    </li>
  </ul>
</body>
</html>
```